Plumbing Company business card design

Create a business card for our plumbing company. Following info needs to be present

Website-prairiepipeworks.com
Email- contact@prairiepipeworks-mail.com
Phone-515-394-2068
Address-4817 NW Cobalt Blvd STE K
Ankeny, Iowa 50347

```html
<!DOCTYPE html>
<html lang="en">
<head>
<meta charset="utf-8">
<title>Prairie Pipeworks – Business Card</title>
<link href="https://fonts.googleapis.com/css2?family=Questrial&display=swap" rel="stylesheet">
<style>
  :root {
    --backdrop: #ececec;
    --card-light: #ffffff;
    --card-dark: #333333;
    --ink-grey: #7a7a7a;
    --mark-grey: #a6a6a6;
    --rule-grey: #8a8a8a;
    --ink-white: #ffffff;
  }
  html, body {
    margin: 0;
    padding: 0;
    width: 1200px;
    height: 1200px;
    overflow: hidden;
    background: var(--backdrop);
    font-family: "Questrial", sans-serif;
  }
  .canvas {
    position: relative;
    width: 1200px;
    height: 1200px;
  }
  .card {
    position: absolute;
    left: 232px;
    width: 735px;
    height: 420px;
    box-sizing: border-box;
    text-align: center;
  }
  .card--contact {
    top: 158px;
    background: var(--card-light);
    color: var(--ink-grey);
  }
  .card--brand {
    top: 622px;
    background: var(--card-dark);
    color: var(--ink-white);
  }
  .brand-ring {
    position: absolute;
    left: 50%;
    transform: translateX(-50%);
    border-radius: 50%;
    box-sizing: border-box;
  }
  .card--contact .brand-ring {
    top: 60px;
    width: 96px;
    height: 96px;
    border: 8px solid var(--mark-grey);
  }
  .card--brand .brand-ring {
    top: 60px;
    width: 124px;
    height: 124px;
    border: 11px solid var(--ink-white);
  }
  .divider {
    position: absolute;
    top: 195px;
    left: 193px;
    width: 382px;
    height: 1px;
    background: var(--rule-grey);
  }
  .contact-list {
    position: absolute;
    top: 209px;
    left: 0;
    width: 100%;
    margin: 0;
    padding: 0;
    list-style: none;
    font-size: 22px;
    line-height: 29.5px;
    letter-spacing: 1px;
  }
  .brand-name {
    position: absolute;
    top: 200px;
    left: 0;
    width: 100%;
    margin: 0;
    font-size: 40px;
    font-weight: 400;
    letter-spacing: 2px;
    text-transform: uppercase;
  }
  .address {
    position: absolute;
    top: 300px;
    left: 0;
    width: 100%;
    margin: 0;
    font-style: normal;
    font-size: 22px;
    line-height: 30px;
    letter-spacing: 1px;
  }
</style>
</head>
<body>
<main class="canvas">
  <section class="card card--contact" aria-label="Card back with contact details">
    <div class="brand-ring" aria-hidden="true"></div>
    <div class="divider"></div>
    <ul class="contact-list">
      <li class="contact-phone">515-394-2068</li>
      <li class="contact-email">contact@prairiepipeworks-mail.com</li>
      <li class="contact-web">www.prairiepipeworks.com</li>
    </ul>
  </section>

  <section class="card card--brand" aria-label="Card front with company name and address">
    <div class="brand-ring" aria-hidden="true"></div>
    <h1 class="brand-name">Prairie Pipeworks</h1>
    <address class="address">
      4817 NW Cobalt Blvd STE K<br>
      Ankeny, Iowa 50347
    </address>
  </section>
</main>
</body>
</html>
```